Treatment Info-Graphic Poster

22 x 28 poster. We need a design for a poster to hang in our treatment rooms that quickly compares different treatments we offer and sets expectations for the patient. Attached is something I very quickly created on Excel, but we would like one that matches our company colors and looks much more polished. I have attached a info-graphic we have had designed prior for reference.

Target Market(s)

Osteoarthritis of the knee patients treatment comparison info graphic for poster

Font styles to use
Serif

Colors
85cae6
f78f20

Requirements
Must have
• Branded treatment comparison table
Nice to have
• Treatment graphics

```html
<!DOCTYPE html>
<html lang="en">
<head>
<meta charset="utf-8">
<title>Knee OA Treatment Comparison</title>
<link href="https://fonts.googleapis.com/css2?family=Crimson+Text:wght@400;600;700&display=swap" rel="stylesheet">
<style>
:root{
  --page:#e6e7e9;
  --poster:#6fb3d2;
  --title:#0f4fa8;
  --orange:#f78f20;
  --orange-deep:#f2450a;
  --label:#1e7fe6;
  --label-edge:#0f5fb8;
  --label-alt:#27a3e4;
  --fine:#8a1e06;
  --note:#1a4fa0;
  --brand:#0f4fa8;
  --white:#ffffff;
}
*{margin:0;padding:0;box-sizing:border-box}
html,body{width:1200px;height:1200px;overflow:hidden;background:var(--page)}
body{font-family:"Crimson Text",Georgia,serif;position:relative}
.poster{position:absolute;left:126px;top:0;width:1083px;height:1370px;transform:scale(.876);transform-origin:0 0;
  background:linear-gradient(180deg,#79bcd9 0%,var(--poster) 60%,#66a9c8 100%);overflow:hidden}
.figure-art{position:absolute;left:120px;top:0;width:700px;height:1370px;
  background:radial-gradient(ellipse at 55% 40%,rgba(210,240,252,.45),rgba(133,202,230,0) 65%)}
.brand-name{position:absolute;left:73px;top:122px;width:214px;text-align:center;font-size:44px;font-weight:600;color:var(--brand);line-height:1}
.title{position:absolute;left:300px;top:112px;font-size:54px;color:var(--title);white-space:nowrap;font-weight:400}
.title b{font-weight:700}
.col{position:absolute;top:248px;width:208px}
.col-head{height:62px;background:var(--orange-deep);color:var(--white);font-size:23px;line-height:1.15;
  display:flex;align-items:center;justify-content:space-between;padding:0 10px 0 16px;border-bottom:3px solid #c23a05}
.col-head.brace{background:var(--orange)}
.col-head svg{width:52px;height:52px;flex:none}
.grades{height:130px;background:linear-gradient(180deg,rgba(130,110,110,.35),rgba(133,202,230,0) 60%);padding-top:6px}
.grade-title{text-align:right;font-size:11px;font-weight:700;color:var(--fine);padding-right:4px;height:22px}
.option{display:flex;justify-content:space-between;font-size:11.5px;color:var(--fine);height:24px;padding:0 10px 0 4px;white-space:nowrap}
.option span:first-child{flex:1;text-align:center}
.row-label{position:absolute;left:46px;width:134px;height:62px;background:var(--label);border-bottom:3px solid var(--label-edge);
  color:var(--white);font-size:14px;font-weight:600;line-height:1.2;text-align:center;display:flex;align-items:center;justify-content:center;padding:0 26px 0 2px}
.row-label.alt{background:var(--label-alt)}
.row-label svg{position:absolute;right:4px;top:4px;width:26px;height:26px}
.cell{position:absolute;height:62px;background:linear-gradient(180deg,rgba(255,255,255,0) 10%,rgba(255,255,255,.55) 100%);
  display:flex;align-items:center;justify-content:center}
.cell svg{width:56px;height:50px}
.note{position:absolute;left:185px;width:848px;top:1190px;text-align:center;font-size:12.5px;color:var(--note);line-height:1.3}
</style>
</head>
<body>
<svg width="0" height="0" style="position:absolute">
  <defs>
    <symbol id="tick" viewBox="0 0 56 50"><path d="M4 30 L14 26 L22 40 Q34 16 54 2 Q38 20 22 48 Z" fill="var(--orange)"/></symbol>
    <symbol id="syringe" viewBox="0 0 52 52"><g fill="none" stroke="#fff" stroke-width="4" stroke-linecap="round"><path d="M10 4 L20 14"/><path d="M15 9 L42 36 L36 42 L9 15"/><path d="M40 40 L50 50"/><path d="M22 22 L28 16 M28 28 L34 22"/></g></symbol>
  </defs>
</svg>
<div class="poster">
  <div class="figure-art" role="img" aria-label="Faint x-ray style illustration of a seated person holding a knee"></div>
  <div class="brand-name">Kinetra</div>
  <h1 class="title"><b>Knee OA</b> Traeatment Comparation</h1>

  <div class="col" style="left:182px">
    <div class="col-head"><span>Hyaluronic<br>Acid (HA)</span><svg><use href="#syringe"/></svg></div>
    <div class="grades"><div class="grade-title">OA Grade</div>
      <div class="option"><span>Single Injection (Velunex One)</span><span>1,2,3,4</span></div>
      <div class="option"><span>Single Injection (Corvalyn)</span><span>1,2,3,4</span></div>
      <div class="option"><span>3 Part Injection Series (Quenvira)</span><span>1,2,3,4</span></div>
      <div class="option"><span>3/4 Part Injection Series (Arvenda)</span><span>1,2,3,4</span></div>
    </div>
  </div>
  <div class="col" style="left:397px">
    <div class="col-head"><span>Platelet Rich<br>Plasma (PRP)</span><svg><use href="#syringe"/></svg></div>
    <div class="grades"><div class="grade-title">OA Grade</div>
      <div class="option"><span>Single Injection (Plaxora)</span><span>1,2</span></div>
      <div class="option"><span>2 Part Injection Series</span><span>3,4</span></div>
    </div>
  </div>
  <div class="col" style="left:610px">
    <div class="col-head"><span>Stem Cell<br>Therapy</span><svg><use href="#syringe"/></svg></div>
    <div class="grades"><div class="grade-title">OA Grade</div>
      <div class="option"><span>Single Injection</span><span>1,2,3,4</span></div>
    </div>
  </div>
  <div class="col" style="left:824px">
    <div class="col-head brace"><span>Knee Brace(s)</span><svg viewBox="0 0 52 52"><g fill="none" stroke="#fff" stroke-width="5" stroke-linecap="round" stroke-linejoin="round"><circle cx="38" cy="8" r="4" fill="#fff"/><path d="M14 20 L26 14 L34 22 L42 26"/><path d="M26 14 L22 32 L32 38 L30 48"/><path d="M22 32 L14 42 L6 40"/></g></svg></div>
    <div class="grades"><div class="grade-title">OA Grade</div>
      <div class="option"><span>Kinebrace 2</span><span>1,2,3,4</span></div>
      <div class="option"><span>Patellar Stabilization</span><span>1,2,3,4</span></div>
    </div>
  </div>

  <div class="row-label" style="top:446px">Cushion &amp;<br>Lubricate<svg viewBox="0 0 26 26"><circle cx="13" cy="13" r="11" fill="#fff"/></svg></div>
  <div class="row-label alt" style="top:513px">Decrease<br>Inflammation<svg viewBox="0 0 26 26"><path d="M13 2 Q22 12 20 18 A7 7 0 0 1 6 18 Q4 12 13 2Z" fill="#fff"/></svg></div>
  <div class="row-label" style="top:579px">Stimulates<br>Synovial<br>Production of HA<svg viewBox="0 0 26 26"><path d="M8 2 L18 12 L12 24" fill="none" stroke="#fff" stroke-width="4"/></svg></div>
  <div class="row-label alt" style="top:646px">Healing<br>Properties<svg viewBox="0 0 26 26"><path d="M13 22 L4 13 A5 5 0 0 1 13 7 A5 5 0 0 1 22 13 Z" fill="#fff"/></svg></div>
  <div class="row-label" style="top:712px">Repairative<br>Properties<svg viewBox="0 0 26 26"><circle cx="13" cy="13" r="9" fill="none" stroke="#fff" stroke-width="3" stroke-dasharray="10 4"/></svg></div>
  <div class="row-label alt" style="top:779px">Potential<br>Cartilage<br>Regeneration<svg viewBox="0 0 26 26"><rect x="4" y="4" width="18" height="18" fill="none" stroke="#fff" stroke-width="3"/></svg></div>
  <div class="row-label" style="top:846px">On Average,<br>Benefits Last 4-6<br>Months<svg viewBox="0 0 26 26"><path d="M13 22 L4 13 A5 5 0 0 1 13 7 A5 5 0 0 1 22 13 Z" fill="#fff"/></svg></div>
  <div class="row-label alt" style="top:912px">On Average,<br>Benefits Last 6-12<br>Months<svg viewBox="0 0 26 26"><path d="M13 22 L4 13 A5 5 0 0 1 13 7 A5 5 0 0 1 22 13 Z" fill="#fff"/></svg></div>
  <div class="row-label" style="top:979px">On Average,<br>Benefits Last 18+<br>Months<svg viewBox="0 0 26 26"><path d="M13 22 L4 13 A5 5 0 0 1 13 7 A5 5 0 0 1 22 13 Z" fill="#fff"/></svg></div>
  <div class="row-label alt" style="top:1046px">Corrects<br>Biomechanics &amp;<br>Stabilizes Joint<svg viewBox="0 0 26 26"><rect x="8" y="3" width="10" height="20" rx="4" fill="#fff"/></svg></div>
  <div class="row-label" style="top:1112px">Covered by<br>MOST Insurance<svg viewBox="0 0 26 26"><path d="M13 3 L22 7 V13 Q22 20 13 24 Q4 20 4 13 V7Z" fill="#fff"/><path d="M13 9 V18 M8.5 13.5 H17.5" stroke="var(--label)" stroke-width="3"/></svg></div>

  <div class="cell" style="left:185px;top:446px;width:207px"><svg><use href="#tick"/></svg></div>
  <div class="cell" style="left:398px;top:446px;width:207px"><svg><use href="#tick"/></svg></div>
  <div class="cell" style="left:610px;top:446px;width:208px"><svg><use href="#tick"/></svg></div>
  <div class="cell" style="left:824px;top:446px;width:209px"></div>
  <div class="cell" style="left:185px;top:513px;width:207px"><svg><use href="#tick"/></svg></div>
  <div class="cell" style="left:398px;top:513px;width:207px"><svg><use href="#tick"/></svg></div>
  <div class="cell" style="left:610px;top:513px;width:208px"><svg><use href="#tick"/></svg></div>
  <div class="cell" style="left:824px;top:513px;width:209px"></div>
  <div class="cell" style="left:185px;top:579px;width:207px"><svg><use href="#tick"/></svg></div>
  <div class="cell" style="left:398px;top:579px;width:207px"><svg><use href="#tick"/></svg></div>
  <div class="cell" style="left:610px;top:579px;width:208px"><svg><use href="#tick"/></svg></div>
  <div class="cell" style="left:824px;top:579px;width:209px"></div>
  <div class="cell" style="left:185px;top:646px;width:207px"></div>
  <div class="cell" style="left:398px;top:646px;width:207px"><svg><use href="#tick"/></svg></div>
  <div class="cell" style="left:610px;top:646px;width:208px"><svg><use href="#tick"/></svg></div>
  <div class="cell" style="left:824px;top:646px;width:209px"></div>
  <div class="cell" style="left:185px;top:712px;width:207px"></div>
  <div class="cell" style="left:398px;top:712px;width:207px"></div>
  <div class="cell" style="left:610px;top:712px;width:208px"><svg><use href="#tick"/></svg></div>
  <div class="cell" style="left:824px;top:712px;width:209px"></div>
  <div class="cell" style="left:185px;top:779px;width:207px"></div>
  <div class="cell" style="left:398px;top:779px;width:207px"></div>
  <div class="cell" style="left:610px;top:779px;width:208px"><svg><use href="#tick"/></svg></div>
  <div class="cell" style="left:824px;top:779px;width:209px"></div>
  <div class="cell" style="left:185px;top:846px;width:207px"><svg><use href="#tick"/></svg></div>
  <div class="cell" style="left:398px;top:846px;width:207px"><svg><use href="#tick"/></svg></div>
  <div class="cell" style="left:610px;top:846px;width:208px"><svg><use href="#tick"/></svg></div>
  <div class="cell" style="left:824px;top:846px;width:209px"><svg><use href="#tick"/></svg></div>
  <div class="cell" style="left:185px;top:912px;width:207px"></div>
  <div class="cell" style="left:398px;top:912px;width:207px"><svg><use href="#tick"/></svg></div>
  <div class="cell" style="left:610px;top:912px;width:208px"><svg><use href="#tick"/></svg></div>
  <div class="cell" style="left:824px;top:912px;width:209px"><svg><use href="#tick"/></svg></div>
  <div class="cell" style="left:185px;top:979px;width:207px"></div>
  <div class="cell" style="left:398px;top:979px;width:207px"></div>
  <div class="cell" style="left:610px;top:979px;width:208px"><svg><use href="#tick"/></svg></div>
  <div class="cell" style="left:824px;top:979px;width:209px"><svg><use href="#tick"/></svg></div>
  <div class="cell" style="left:185px;top:1046px;width:207px"></div>
  <div class="cell" style="left:398px;top:1046px;width:207px"></div>
  <div class="cell" style="left:610px;top:1046px;width:208px"></div>
  <div class="cell" style="left:824px;top:1046px;width:209px"><svg><use href="#tick"/></svg></div>
  <div class="cell" style="left:185px;top:1112px;width:207px"><svg><use href="#tick"/></svg></div>
  <div class="cell" style="left:398px;top:1112px;width:207px"></div>
  <div class="cell" style="left:610px;top:1112px;width:208px"></div>
  <div class="cell" style="left:824px;top:1112px;width:209px"><svg><use href="#tick"/></svg></div>

  <p class="note">Treatment outcomes vary by individual. Treatment benefits and length of efficacy are not guaranteed. In some cases, patient's do not respond to treatment.<br>Multiple treatments may be recommended or necessary for the best outcomes.</p>
</div>
</body>
</html>
```